Business Card Design Project

A new design for our business cards for a small casting/talent agency, we would like to incorporate the logo and brand colors within the design, below are the information that should be on the card

(Name)
(Title)

Corvel Arta FZ-LLC
Brindle Quay Park
Building 27, Suite 418
Dubai, UAE
PO Box 871465
+97140000000
info@CorvelArta-example.com

Target Market(s)

production companies, film makers, media, entertainment industry

Industry/Entity Type

Business

Requirements
Must have
• logo, logo colors
Nice to have
• cutting edge design, sleek and modern
Should not have
• playful, funky, congested

```html
<!DOCTYPE html>
<html lang="en">
<head>
<meta charset="utf-8">
<title>Corvel Arta – Business Card</title>
<link href="https://fonts.googleapis.com/css2?family=Montserrat:wght@400;700&display=swap" rel="stylesheet">
<style>
  :root {
    --stage: #1b1d22;
    --navy: #0f2f6b;
    --navy-deep: #081d47;
    --navy-light: #1d4a9a;
    --paper: #ffffff;
    --mist: #d5d9de;
    --grey-text: #6b6f76;
    --ink: #16326e;
  }
  * { box-sizing: border-box; margin: 0; padding: 0; }
  html, body {
    width: 1200px; height: 675px; overflow: hidden;
    background: var(--stage);
    font-family: "Montserrat", sans-serif;
  }
  .canvas {
    width: 1200px; height: 675px;
    display: flex; align-items: center; justify-content: center; gap: 60px;
  }
  .card {
    position: relative; width: 510px; height: 291px;
    border-radius: 4px; overflow: hidden;
    box-shadow: 0 12px 30px rgba(0,0,0,.45);
  }
  /* Front */
  .card-front { background: var(--paper); }
  .front-mark {
    position: absolute; right: -70px; top: -60px;
    width: 300px; height: 300px; border-radius: 50%;
    background: var(--mist); opacity: .75;
  }
  .edge-bar {
    position: absolute; left: 0; bottom: 0;
    width: 8px; height: 110px; background: var(--mist);
  }
  .identity { position: absolute; left: 34px; top: 104px; }
  .person-name { font-weight: 700; font-size: 24px; color: var(--ink); letter-spacing: .2px; }
  .person-title { font-size: 9px; color: var(--grey-text); margin-top: 2px; }
  .contact { position: absolute; left: 34px; bottom: 34px; font-size: 10.5px; line-height: 1.45; color: var(--grey-text); }
  .company { font-weight: 700; color: var(--ink); font-size: 10.5px; }
  .contact-line { display: flex; align-items: center; gap: 7px; }
  .contact-line svg { width: 9px; height: 9px; fill: var(--ink); flex: none; }
  .contact-lines { margin-top: 6px; }
  /* Back */
  .card-back {
    background: radial-gradient(ellipse at 50% 40%, var(--navy-light) 0%, var(--navy) 55%, var(--navy-deep) 100%);
    display: flex; flex-direction: column; align-items: center; justify-content: center;
  }
  .logo-badge {
    width: 170px; height: 170px; border-radius: 50%;
    background: var(--navy);
    border: 2px solid rgba(255,255,255,.85);
    display: flex; align-items: center; justify-content: center;
  }
  .brand-name { font-size: 20px; font-weight: 400; color: var(--paper); letter-spacing: .5px; }
  .website { margin-top: 18px; font-size: 13px; color: var(--paper); letter-spacing: .6px; }
</style>
</head>
<body>
<main class="canvas">
  <section class="card card-front">
    <div class="front-mark" aria-hidden="true"></div>
    <div class="edge-bar" aria-hidden="true"></div>
    <div class="identity">
      <p class="person-name">Elias Marrow</p>
      <p class="person-title">President &amp; CEO</p>
    </div>
    <div class="contact">
      <p class="company">Corvel Arta FZ-LLC</p>
      <p>Brindle Quay Park, Building 27, Suite 418</p>
      <p>Dubai, UAE, PO Box 871465</p>
      <div class="contact-lines">
        <p class="contact-line">
          <svg viewBox="0 0 10 10" aria-hidden="true"><path d="M1 3 Q5 0 9 3 L8 4.5 L6.5 3.8 L6.5 3 Q5 2.6 3.5 3 L3.5 3.8 L2 4.5 Z M2.5 5 H7.5 L8.5 9 H1.5 Z"/></svg>
          +97140000000
        </p>
        <p class="contact-line">
          <svg viewBox="0 0 10 10" aria-hidden="true"><path d="M0.5 2 H9.5 V8.5 H0.5 Z M1 2.4 L5 5.6 L9 2.4" stroke="#fff" stroke-width=".8"/></svg>
          info@CorvelArta-example.com
        </p>
      </div>
    </div>
  </section>

  <section class="card card-back">
    <div class="logo-badge"><span class="brand-name">Corvel Arta</span></div>
    <p class="website">www.CorvelArta-example.com</p>
  </section>
</main>
</body>
</html>
```